Create Website for new Home services company

We need a website built for a new home services company we are primarily a surface refinishing company that repairs cracks in tubs and resurfaces tubs, sinks or vanities also repainting cabinets as well.

```html
<!DOCTYPE html>
<html lang="en">
<head>
<meta charset="utf-8">
<title>Harlow Home Services</title>
<link href="https://fonts.googleapis.com/css2?family=Archivo:wght@400;500;700;800&family=Open+Sans:wght@400;600;700&display=swap" rel="stylesheet">
<style>
:root{
  --orange:#e8722a;
  --orange-dark:#d9621d;
  --blue:#1f6fb3;
  --blue-deep:#1a64a6;
  --grey-head:#5a5a5a;
  --text:#333;
  --muted:#8a8a8a;
  --pale:#eef4f8;
  --footer:#2b2b2b;
  --white:#fff;
}
*{box-sizing:border-box;margin:0;padding:0}
html,body{width:1200px;height:4310px;overflow:hidden}
body{font-family:"Open Sans",sans-serif;color:var(--text);background:var(--white);position:relative}
.abs{position:absolute}
.btn{position:absolute;display:flex;align-items:center;justify-content:center;border-radius:30px;color:#fff;font-weight:700;font-size:14px;font-family:"Open Sans",sans-serif}
.btn-orange{background:var(--orange)}
.btn-blue{background:var(--blue)}
.title{position:absolute;left:0;width:1200px;text-align:center;font-family:"Archivo",sans-serif;font-size:38px;color:var(--grey-head);letter-spacing:1px}
.title b{font-weight:800}
.title span{font-weight:400;color:var(--blue)}
.title-rule{position:absolute;left:535px;width:130px;height:3px;background:var(--orange)}
.ph{position:absolute}

/* social link buttons: plain circles with a neutral dot, no network marks */
.social{position:absolute;width:34px;height:34px;border-radius:50%;display:flex;align-items:center;justify-content:center}
.social::after{content:"";width:10px;height:10px;border-radius:50%}
.social.o{background:var(--orange)}
.social.o::after{background:#fff}
.social.w{background:#fff;box-shadow:0 1px 6px rgba(0,0,0,.2)}
.social.w::after{background:var(--blue)}

/* header */
.header{position:absolute;top:0;left:0;width:1200px;height:127px;background:#fff}
.brand{left:110px;top:30px;font-family:"Archivo",sans-serif;line-height:1.2}
.brand .b1{font-size:30px;font-weight:800;color:var(--grey-head);display:block}
.brand .b2{font-size:30px;font-weight:400;color:var(--blue);display:block}
.call{left:795px;top:25px}
.call small{font-size:11px;color:#555;display:block}
.call strong{font-size:16px;color:var(--orange);font-weight:700}
.nav{position:absolute;top:88px;left:557px;display:flex;gap:37px;font-size:14px;font-weight:600;color:#222}
.nav .on{color:var(--orange)}

/* hero */
.hero{position:absolute;top:127px;left:0;width:1200px;height:559px;background:linear-gradient(90deg,#eeeeee 0%,#e4e4e3 45%,#c8c6c2 70%,#d7d6d3 100%)}
.hero h1{position:absolute;left:110px;top:155px;font-family:"Archivo",sans-serif;font-size:46px;line-height:1.12}
.hero h1 b{font-weight:800;color:var(--grey-head);display:block}
.hero h1 span{font-weight:400;color:var(--blue);display:block}
.hero p{position:absolute;left:110px;top:270px;width:460px;font-size:17px;line-height:1.65;color:#333}

/* about */
.about h2{position:absolute;left:670px;top:865px;font-family:"Archivo",sans-serif;font-size:46px;font-weight:500;color:var(--grey-head);padding-left:26px}
.about h2::before{content:"";position:absolute;left:0;top:12px;width:4px;height:32px;background:var(--orange)}
.about p{position:absolute;left:670px;width:418px;font-size:13px;line-height:26px;color:var(--muted);text-align:justify}

/* services */
.services{position:absolute;top:1383px;left:0;width:1200px;height:763px;background:var(--pale)}
.svc-label{position:absolute;width:260px;text-align:center;font-size:14px;font-weight:700;color:#555;line-height:25px}
.svc-rule{position:absolute;width:50px;height:3px;background:var(--blue)}
.svc-text{position:absolute;width:266px;text-align:center;font-size:13px;line-height:24px;color:var(--muted)}
.plus{position:absolute;width:36px;height:36px;border-radius:50%;background:var(--orange);color:#fff;font-weight:700;font-size:20px;display:flex;align-items:center;justify-content:center}

/* testimonials */
.reviews{position:absolute;top:2146px;left:0;width:1200px;height:462px;background:var(--orange)}
.reviews .title{color:#fff}
.reviews .title span{color:#fff}
.card{position:absolute;top:177px;width:314px;height:190px;background:#fff;border-radius:4px}
.avatar{position:absolute;left:16px;top:16px;width:62px;height:62px;border-radius:50%;background:linear-gradient(135deg,#c9c2b8,#8f8678);border:3px solid #e6e6e6}
.card h4{position:absolute;left:97px;top:36px;font-family:"Archivo",sans-serif;font-size:16px;font-weight:500;color:#333}
.stars{position:absolute;left:97px;top:58px;color:var(--orange);font-size:11px;letter-spacing:1px}
.quote{position:absolute;right:16px;top:28px;font-family:"Archivo",sans-serif;font-size:64px;font-weight:800;color:#d6dde4;line-height:1}
.card p{position:absolute;left:16px;top:102px;width:285px;font-size:13px;line-height:23px;color:var(--muted)}
.circ-arrow{position:absolute;width:34px;height:34px;border-radius:50%;background:#fff;display:flex;align-items:center;justify-content:center}

/* blog */
.post{position:absolute;background:#fff;box-shadow:0 2px 14px rgba(0,0,0,.1)}
.date{position:absolute;font-size:11px;color:#555;display:flex;align-items:center;gap:10px}
.date i{display:block;width:24px;height:24px;border-radius:50%;background:var(--blue)}
.post h3{position:absolute;font-family:"Archivo",sans-serif;font-size:16px;font-weight:500;color:#333;line-height:24px}
.post p{position:absolute;font-size:13px;line-height:25px;color:var(--muted)}
.more{position:absolute;font-size:14px;font-weight:700;color:var(--orange);text-decoration:underline}

/* contact */
.contact{position:absolute;top:3370px;left:0;width:1200px;height:564px;background:var(--blue)}
.contact .title{color:#fff}
.contact .title span{color:#fff}
.info-ic{position:absolute;width:64px;height:64px;border-radius:50%;background:#fff;display:flex;align-items:center;justify-content:center}
.info{position:absolute;color:#fff;font-size:12px;line-height:20px}
.info b{display:block;font-size:12px;margin-bottom:8px}
.field{position:absolute;background:#fff;border-radius:3px;font-size:13px;color:#777;padding:13px 16px}

/* footer */
.footer{position:absolute;top:3934px;left:0;width:1200px;height:376px;background:var(--footer);color:#fff}
.footer h5{position:absolute;font-size:14px;font-weight:700;letter-spacing:.3px}
.flink{position:absolute;font-size:13px;display:flex;align-items:center;gap:16px}
.flink i{display:block;width:12px;height:12px;border-radius:50%;background:var(--orange)}
.fci{position:absolute;font-size:13px;line-height:21px}
.fci b{display:block}
</style>
</head>
<body>

<header class="header">
  <div class="abs brand"><span class="b1">HARLOW HOME</span><span class="b2">SERVICES</span></div>
  <svg class="abs" style="left:740px;top:22px" width="40" height="40" viewBox="0 0 40 40"><path d="M8 6c3-2 5 0 7 4 1 2 0 4-2 5 1 4 4 8 8 10 1-2 3-3 5-2 4 2 6 4 4 7-2 4-7 5-12 2C11 28 5 20 5 13c0-3 1-5 3-7z" fill="var(--blue)"/><path d="M24 6a12 12 0 0 1 10 10M24 12a6 6 0 0 1 5 5" stroke="var(--blue)" stroke-width="2" fill="none"/></svg>
  <div class="abs call"><small>CALL US TODAY:</small><strong>+ 1 (555) 014 2290</strong></div>
  <div class="social o" style="left:971px;top:27px"></div>
  <div class="social w" style="left:1013px;top:27px"></div>
  <div class="social w" style="left:1054px;top:27px"></div>
  <nav class="nav"><span class="on">HOME</span><span>ABOUT US</span><span>SERVICES OFFERED</span><span>RESOURCES</span><span>CONTACT</span></nav>
</header>

<section class="hero" role="img" aria-label="Technician in blue overalls installing a faucet at a white bathroom sink">
  <h1><b>HARLOW HOME</b><span>SERVICES</span></h1>
  <p>Lorem ipsum dolor sit amet consectetur adipiscing sed do eiusmod temetur adipor incidea.</p>
  <div class="btn btn-orange" style="left:110px;top:345px;width:136px;height:49px">BOOK NOW</div>
</section>

<section class="about">
  <div class="ph" role="img" aria-label="Hand tightening a chrome sink drain pipe with a wrench" style="left:110px;top:807px;width:344px;height:385px;background:linear-gradient(135deg,#e9e7e3,#b9b3aa)"></div>
  <svg class="abs" style="left:187px;top:1199px" width="124" height="44">
    <defs><pattern id="dots" width="12.4" height="11" patternUnits="userSpaceOnUse"><circle cx="2" cy="2" r="1.6" fill="#c8ccd2"/></pattern></defs>
    <rect width="124" height="44" fill="url(#dots)"/>
  </svg>
  <div class="ph" role="img" aria-label="Worker in black cap refinishing a white bathtub edge" style="left:315px;top:979px;width:274px;height:290px;background:linear-gradient(135deg,#f2f2f2,#9a9a9a);border:6px solid #fff"></div>
  <h2>ABOUT US</h2>
  <p style="top:938px">Lorem ipsum dolor sit amet, consectetur adipiscing elit, sed do eiusm od tempor incididunt ut labore et dolore magna aliqua. Ut enim ad minim veniam, quis nostrud exercitation ullamco laboris nisi ut aliquip ex ea commodo exercitation uatea.</p>
  <p style="top:1050px">Tempor incididunt ut labore et dolore magna aliqua. Ut enim ad minim veniam, quis nostrud exercitation ullamco laboris nisi ut aliquip ex ea commodo exercitation uatea.</p>
  <div class="btn btn-orange" style="left:670px;top:1158px;width:145px;height:47px;font-size:13px">LEARN MORE</div>
</section>

<section class="services">
  <div class="title" style="top:60px"><b>SERVICES</b> <span>OFFERED</span></div>
  <div class="title-rule" style="top:110px"></div>
  <svg class="abs" style="left:50px;top:348px" width="20" height="24"><path d="M14 2 4 12l10 10" stroke="#aaa" stroke-width="2" fill="none"/></svg>
  <svg class="abs" style="left:1132px;top:348px" width="20" height="24"><path d="M6 2l10 10L6 22" stroke="#444" stroke-width="2" fill="none"/></svg>

  <svg class="abs" role="img" aria-label="Technician repairing a crack in a bathtub" style="left:110px;top:165px" width="310" height="270"><path d="M24 262A155 155 0 1 1 286 262Q155 180 24 262z" fill="#6f8fb5"/></svg>
  <svg class="abs" role="img" aria-label="Hands fitting a wrench to a sink drain" style="left:444px;top:165px" width="310" height="270"><path d="M24 262A155 155 0 1 1 286 262Q155 180 24 262z" fill="#b9b5b0"/></svg>
  <svg class="abs" role="img" aria-label="Gloved hand painting a cabinet panel white" style="left:779px;top:165px" width="310" height="270"><path d="M24 262A155 155 0 1 1 286 262Q155 180 24 262z" fill="#d8b884"/></svg>

  <div class="svc-label" style="left:135px;top:407px">REPAIRS CRACKS<br>IN TUBS</div>
  <div class="svc-label" style="left:469px;top:407px">RESURFACES<br>SINKS</div>
  <div class="svc-label" style="left:804px;top:407px">REPAINTING<br>CABINETS</div>
  <div class="svc-rule" style="left:240px;top:461px"></div>
  <div class="svc-rule" style="left:574px;top:461px"></div>
  <div class="svc-rule" style="left:909px;top:461px"></div>
  <div class="svc-text" style="left:132px;top:480px">Sed ut perspiciatis unde omnis iste nat us error sit voluptatem accusantium doloremque laudantea.</div>
  <div class="svc-text" style="left:466px;top:480px">Sed ut perspiciatis unde omnis iste nat us error sit voluptatem accusantium doloremque laudantea.</div>
  <div class="svc-text" style="left:801px;top:480px">Sed ut perspiciatis unde omnis iste nat us error sit voluptatem accusantium doloremque laudantea.</div>
  <div class="plus" style="left:247px;top:566px">+</div>
  <div class="plus" style="left:581px;top:566px">+</div>
  <div class="plus" style="left:916px;top:566px">+</div>
  <div class="btn btn-blue" style="left:511px;top:648px;width:179px;height:45px;font-size:13px">VIEW ALL SERVICES</div>
</section>

<section class="reviews">
  <div class="title" style="top:84px;font-size:32px"><b>WHAT OUR</b> <span>CUSTOMERS SAY</span></div>
  <div class="circ-arrow" style="left:38px;top:254px"><svg width="12" height="14"><path d="M9 1 3 7l6 6" stroke="var(--blue)" stroke-width="2" fill="none"/></svg></div>
  <div class="circ-arrow" style="left:1127px;top:254px"><svg width="12" height="14"><path d="M3 1l6 6-6 6" stroke="var(--blue)" stroke-width="2" fill="none"/></svg></div>
  <div class="card" style="left:110px"><div class="avatar" role="img" aria-label="Customer portrait"></div><h4>JOHN SMITH</h4><div class="stars">★★★★★</div><div class="quote">&#8221;</div><p>At vero eos et accusamus et iusto odio digni ssimos duci lormus qui blanditiis praesentium voluptatum deleniitea.</p></div>
  <div class="card" style="left:444px"><div class="avatar" role="img" aria-label="Customer portrait"></div><h4>JOHN SMITH</h4><div class="stars">★★★★★</div><div class="quote">&#8221;</div><p>At vero eos et accusamus et iusto odio digni ssimos duci lormus qui blanditiis praesentium voluptatum deleniitea.</p></div>
  <div class="card" style="left:775px"><div class="avatar" role="img" aria-label="Customer portrait"></div><h4>JOHN SMITH</h4><div class="stars">★★★★★</div><div class="quote">&#8221;</div><p>At vero eos et accusamus et iusto odio digni ssimos duci lormus qui blanditiis praesentium voluptatum deleniitea.</p></div>
</section>

<section class="blog">
  <div class="title" style="top:2710px;font-weight:500">LATEST <span>BLOG</span></div>
  <div class="title-rule" style="top:2760px;width:70px;left:565px"></div>

  <article class="post" style="left:110px;top:2809px;width:481px;height:447px">
    <div class="ph" role="img" aria-label="Plumber in cap clearing a kitchen sink drain" style="left:9px;top:8px;width:464px;height:283px;background:linear-gradient(135deg,#eceae6,#8b8d92)"></div>
    <div class="date" style="left:30px;top:309px"><i></i>08 APR 2023</div>
    <h3 style="left:30px;top:349px;width:420px">LOREM IPSUM DOLOR SIT AMET, CONSECTETUR ADIPISCING ELIT, SED DO EIUSMOD</h3>
    <div class="more" style="left:30px;top:406px">READ MORE</div>
  </article>

  <article class="post" style="left:608px;top:2809px;width:480px;height:214px">
    <div class="ph" role="img" aria-label="Hands tightening a chrome drain pipe" style="left:10px;top:10px;width:196px;height:196px;background:linear-gradient(135deg,#ecebea,#a9a49e)"></div>
    <div class="date" style="left:226px;top:26px"><i></i>08 APR 2023</div>
    <h3 style="left:226px;top:62px;width:230px">LOREM IPSUM DOLOR SIT AMET, CONSEA</h3>
    <p style="left:226px;top:114px;width:240px">Sed ut perspiciatis unde omnis iste natus error sit voluptatem</p>
    <div class="more" style="left:226px;top:171px">READ MORE</div>
  </article>

  <article class="post" style="left:608px;top:3042px;width:480px;height:214px">
    <div class="ph" role="img" aria-label="Workman holding a paint can in a workshop" style="left:10px;top:10px;width:196px;height:196px;background:linear-gradient(135deg,#7b8796,#4a4038)"></div>
    <div class="date" style="left:226px;top:26px"><i></i>08 APR 2023</div>
    <h3 style="left:226px;top:62px;width:230px">LOREM IPSUM DOLOR SIT AMET, CONSEA</h3>
    <p style="left:226px;top:114px;width:240px">Sed ut perspiciatis unde omnis iste natus error sit voluptatem</p>
    <div class="more" style="left:226px;top:171px">READ MORE</div>
  </article>
</section>

<section class="contact">
  <div class="title" style="top:122px;font-size:36px"><b>GET IN</b> <span>TOUCH</span></div>
  <div class="info-ic" style="left:197px;top:165px"><svg width="26" height="26" viewBox="0 0 26 26"><path d="M13 2a7 7 0 0 1 7 7c0 5-7 12-7 12S6 14 6 9a7 7 0 0 1 7-7z" fill="none" stroke="var(--orange)" stroke-width="2"/><circle cx="13" cy="9" r="2.5" fill="var(--orange)"/><path d="M5 23h16" stroke="var(--orange)" stroke-width="2"/></svg></div>
  <div class="info" style="left:289px;top:170px"><b>LOCATION:</b>465, Lorum Ipsum Dolore,<br>United States</div>
  <div class="info-ic" style="left:480px;top:165px"><svg width="26" height="26" viewBox="0 0 26 26"><path d="M6 3c2-1 4 0 5 3 1 2 0 3-1 4 1 3 3 5 6 6 1-1 2-2 4-1 3 1 4 3 3 5-2 3-6 3-10 1C8 19 4 14 4 9c0-3 1-5 2-6z" fill="none" stroke="var(--orange)" stroke-width="2"/></svg></div>
  <div class="info" style="left:572px;top:178px"><b>PHONE:</b>+1 (555) 014 2290</div>
  <div class="info-ic" style="left:726px;top:165px"><svg width="28" height="22" viewBox="0 0 28 22"><rect x="2" y="2" width="24" height="18" rx="2" fill="var(--orange)"/><path d="M2 3l12 9 12-9" stroke="#fff" stroke-width="2" fill="none"/></svg></div>
  <div class="info" style="left:815px;top:178px"><b>EMAIL ADDRESS:</b>info@harlowhomeservices.com</div>
  <div class="field" style="left:166px;top:264px;width:281px;height:49px">Full Name</div>
  <div class="field" style="left:459px;top:264px;width:281px;height:49px">Phone Number</div>
  <div class="field" style="left:752px;top:264px;width:283px;height:49px">Email Address</div>
  <div class="field" style="left:166px;top:326px;width:869px;height:91px">Message...!</div>
  <div class="btn btn-orange" style="left:519px;top:437px;width:161px;height:47px;font-size:13px">SEND MESSAGE</div>
</section>

<footer class="footer">
  <div class="abs brand" style="top:146px;line-height:1.25"><span class="b1" style="color:#fff;font-size:26px">HARLOW HOME</span><span class="b2" style="font-size:26px">SERVICES</span></div>
  <h5 style="left:346px;top:65px">QUICK LINKS</h5>
  <div class="flink" style="left:346px;top:106px"><i></i>Home</div>
  <div class="flink" style="left:346px;top:146px"><i></i>About Us</div>
  <div class="flink" style="left:346px;top:185px"><i></i>Services Offered</div>
  <div class="flink" style="left:346px;top:225px"><i></i>Resources</div>
  <div class="flink" style="left:346px;top:264px"><i></i>Contact</div>
  <h5 style="left:545px;top:65px">CONTACT INFO</h5>
  <svg class="abs" style="left:545px;top:103px" width="12" height="16"><path d="M6 1a5 5 0 0 1 5 5c0 4-5 9-5 9S1 10 1 6a5 5 0 0 1 5-5z" fill="var(--orange)"/></svg>
  <div class="fci" style="left:578px;top:100px"><b>ADDRESS:</b>465, Lorum Ipsum DoloreSed,<br>Unied States</div>
  <svg class="abs" style="left:545px;top:168px" width="14" height="14"><path d="M3 1c1 0 2 1 3 3L5 6c1 2 2 3 4 4l2-1c2 1 3 2 3 3-1 2-3 2-5 1C5 11 2 8 1 5 0 3 1 1 3 1z" fill="var(--orange)"/></svg>
  <div class="fci" style="left:578px;top:166px"><b>PHONE:</b>+1 (555) 014 2290</div>
  <svg class="abs" style="left:545px;top:226px" width="14" height="11"><rect width="14" height="11" rx="1" fill="var(--orange)"/></svg>
  <div class="fci" style="left:578px;top:224px"><b>EMAIL:</b>info@harlowhomeservices.com</div>
  <h5 style="left:805px;top:65px">NEWSLETTER SIGNUP</h5>
  <div class="abs" style="left:805px;top:110px;width:283px;height:44px;border-radius:24px;background:#fff;border:2px solid #fff">
    <span class="abs" style="left:16px;top:11px;font-size:13px;color:#555">Email Address</span>
    <div class="btn btn-orange" style="right:2px;top:2px;width:94px;height:36px;font-size:13px;font-weight:400">SIGN UP</div>
  </div>
  <div class="social o" style="left:811px;top:187px;width:40px;height:40px"></div>
  <div class="social w" style="left:859px;top:187px;width:40px;height:40px"></div>
  <div class="social w" style="left:909px;top:187px;width:40px;height:40px"></div>
  <div class="abs" style="left:110px;top:315px;width:978px;height:1px;background:#444"></div>
  <div class="abs" style="left:0;top:330px;width:1200px;text-align:center;font-size:12px">© 2023 HARLOW HOME SERVICES &nbsp;|&nbsp; All Rights Reserved</div>
</footer>

</body>
</html>
```